Live Scavenger Hunt Mobile Platform needs a face lift!

We have been live for the past year and serving some very large customers, however, we are a group of developers that lack any real design skills. We are looking for a designer to help take our apps look and feel to the next level.

You can see the app in the Quellmart store here: https://apps.quellmart.example/us/app/trovanta.app/id913582047?mt=8

And in brindle pix here: https://shop.brindlepix.example/store/apps/developer?id=trovantaapp&hl=en

We do not plan to change the UX of app, but rather just the aesthetics. Ideally, if this project works out well we would work with the same designer to update our site: http://trovanta.app

You can watch a video of how the platform works here:
http://clipsharva.example/user8831054/elf-themed-christmas-scavenger-hunt

I have included the PSD files we used for the current mobile apps along with the PSD for our logo. In terms of colors we do like the current green and orange/red found in the logo. We have started to gravitate towards a brown textured background, but am open to change on this.

Industry/Entity Type

Store

Requirements
Must have
• The home screen should have a larger focus on getting started vs. the other three categories of 'hunts, settings and help'. We worked with a Marlowbrook designer when re-skinning the app for the experience an we liked how they did this.

https://apps.quellmart.example/us/app/pantry-quest/id730418855?mt=8
Nice to have
• - Custom web font (Some what playful) I am using Hobo Std in our logo
- Textured background
- Fun and playful, yet clean and clear. (Yes I realize that is a challenge)

```html
<!DOCTYPE html>
<html lang="en">
<head>
<meta charset="utf-8">
<title>Trovanta – App Screens</title>
<link rel="stylesheet" href="https://fonts.googleapis.com/css2?family=Fredoka:wght@600&family=Roboto+Condensed:ital,wght@0,400;0,700;1,700&family=Arimo:wght@400;700&display=swap">
<style>
  :root {
    --page-bg: #070403;
    --page-glow: #2a130a;
    --wood-dark: #1c0d07;
    --wood-mid: #3a1a0d;
    --wood-light: #4a2313;
    --header-bg: #241008;
    --status-bg: #d9d9d9;
    --status-text: #111;
    --green: #3f9a1c;
    --green-light: #5fbf2a;
    --green-text: #4db21f;
    --orange: #c8400f;
    --orange-light: #e2561c;
    --orange-text: #e0541d;
    --tab-brown: #8a3312;
    --white: #ffffff;
    --muted: #8b7d74;
  }
  * { box-sizing: border-box; margin: 0; padding: 0; }
  html, body { width: 1200px; height: 1073px; overflow: hidden; }
  body {
    background: radial-gradient(ellipse 520px 480px at 600px 620px, var(--page-glow), var(--page-bg) 75%);
    font-family: "Arimo", Arial, sans-serif;
    color: var(--white);
    position: relative;
  }
  .brand-title {
    position: absolute; top: 50px; left: 0; width: 1200px;
    text-align: center;
    font-family: "Fredoka", sans-serif; font-weight: 600;
    font-size: 52px; color: var(--white); letter-spacing: 1px;
  }
  .screen {
    position: absolute; top: 384px; width: 244px; height: 428px;
    overflow: hidden; border-radius: 2px;
  }
  .screen--home { left: 298px; }
  .screen--challenges { left: 636px; }
  .screen__wood {
    position: absolute; inset: 0;
    background: linear-gradient(90deg, var(--wood-dark), var(--wood-mid) 30%, var(--wood-light) 50%, var(--wood-mid) 70%, var(--wood-dark));
  }
  .status-bar {
    position: absolute; top: 0; left: 0; right: 0; height: 15px;
    background: var(--status-bg); color: var(--status-text);
    font-size: 9px; text-align: center; line-height: 15px;
  }
  .status-bar__signal { position: absolute; left: 6px; top: 4px; }
  .status-bar__battery { position: absolute; right: 6px; top: 4px; }
  .app-header {
    position: absolute; top: 15px; left: 0; right: 0; height: 51px;
    background: var(--header-bg);
    display: flex; align-items: center; justify-content: center;
  }
  .app-header__name {
    font-family: "Fredoka", sans-serif; font-weight: 600;
    font-size: 24px; color: var(--white);
  }
  .app-header__icon { position: absolute; top: 17px; }
  .app-header__icon--back { left: 12px; }
  .app-header__icon--settings { right: 12px; }
  .btn {
    position: absolute; display: flex; align-items: center; justify-content: center; gap: 8px;
    color: var(--white); font-family: "Roboto Condensed", sans-serif;
    border-radius: 3px; text-transform: uppercase;
  }
  .btn--start {
    left: 49px; top: 128px; width: 152px; height: 35px;
    background: linear-gradient(var(--green-light), var(--green));
    font-size: 22px; box-shadow: 0 2px 4px rgba(0,0,0,.6);
  }
  .btn--menu {
    left: 74px; width: 101px; height: 23px;
    background: linear-gradient(var(--orange-light), var(--orange));
    font-size: 13px; box-shadow: 0 1px 3px rgba(0,0,0,.6);
  }
  .btn--hunt { top: 198px; }
  .btn--settings { top: 233px; }
  .btn--help { top: 266px; }
  .tabs { position: absolute; top: 66px; left: 0; right: 0; height: 19px; display: flex; }
  .tab {
    flex: 1; text-align: center; line-height: 19px;
    font-family: "Roboto Condensed", sans-serif; font-size: 8px; text-transform: uppercase;
  }
  .tab--challenges { background: var(--tab-brown); }
  .tab--completed { background: var(--green); }
  .challenge-list { position: absolute; top: 92px; left: 0; right: 0; list-style: none; }
  .challenge {
    position: relative; height: 65px; padding: 12px 10px;
    background: linear-gradient(rgba(0,0,0,.35) 0 50%, rgba(0,0,0,.1) 50%);
    border-bottom: 1px solid rgba(0,0,0,.5);
  }
  .challenge__title { font-size: 13px; font-weight: 700; }
  .challenge__points { font-size: 7px; color: var(--orange-text); margin-top: 3px; }
  .challenge__chevron { position: absolute; right: 9px; top: 18px; }
  .stats {
    position: absolute; top: 300px; left: 0; right: 0;
    display: grid; grid-template-columns: 114px 1fr; row-gap: 15px; column-gap: 12px;
    font-family: "Roboto Condensed", sans-serif;
  }
  .stats__label { text-align: right; color: var(--muted); font-size: 13px; }
  .stats__value { color: var(--green-text); font-size: 13px; font-weight: 700; font-style: italic; }
</style>
</head>
<body>
  <h1 class="brand-title">Trovanta</h1>

  <section class="screen screen--home" aria-label="Home screen">
    <div class="screen__wood" role="img" aria-label="Dark brown wood grain background texture"></div>
    <div class="status-bar">
      <svg class="status-bar__signal" width="22" height="7" viewBox="0 0 22 7"><rect x="0" y="5" width="2" height="2" fill="#111"/><rect x="3" y="4" width="2" height="3" fill="#111"/><rect x="6" y="3" width="2" height="4" fill="#111"/><rect x="9" y="1" width="2" height="6" fill="#111"/></svg>
      9:41 AM
      <svg class="status-bar__battery" width="16" height="7" viewBox="0 0 16 7"><rect x="0.5" y="0.5" width="13" height="6" fill="none" stroke="#111"/><rect x="2" y="2" width="10" height="3" fill="#111"/><rect x="14" y="2" width="1.5" height="3" fill="#111"/></svg>
    </div>
    <header class="app-header"><span class="app-header__name">Trovanta</span></header>

    <a class="btn btn--start"><svg width="12" height="13" viewBox="0 0 12 13"><path d="M0 0 L12 6.5 L0 13Z" fill="#fff"/></svg>Start</a>
    <a class="btn btn--menu btn--hunt"><svg width="11" height="11" viewBox="0 0 11 11"><circle cx="7" cy="1.5" r="1.5" fill="#fff"/><path d="M6 3 L3 6 L1 6 M6 3 L5 7 L7 11 M5 7 L2 10 M6 3 L9 6 L10 5" stroke="#fff" stroke-width="1.3" fill="none"/></svg>Hunt</a>
    <a class="btn btn--menu btn--settings"><svg width="9" height="9" viewBox="0 0 10 10"><circle cx="5" cy="5" r="3.5" fill="none" stroke="#fff" stroke-width="2" stroke-dasharray="2 1.2"/><circle cx="5" cy="5" r="1.2" fill="#fff"/></svg>Settings</a>
    <a class="btn btn--menu btn--help"><svg width="7" height="10" viewBox="0 0 7 10"><circle cx="3.5" cy="3.5" r="3" fill="none" stroke="#fff"/><rect x="2.5" y="7" width="2" height="2.5" fill="#fff"/></svg>Help</a>
  </section>

  <section class="screen screen--challenges" aria-label="Challenges screen">
    <div class="screen__wood" role="img" aria-label="Dark brown wood grain background texture"></div>
    <div class="status-bar">
      <svg class="status-bar__signal" width="22" height="7" viewBox="0 0 22 7"><rect x="0" y="5" width="2" height="2" fill="#111"/><rect x="3" y="4" width="2" height="3" fill="#111"/><rect x="6" y="3" width="2" height="4" fill="#111"/><rect x="9" y="1" width="2" height="6" fill="#111"/></svg>
      9:41 AM
      <svg class="status-bar__battery" width="16" height="7" viewBox="0 0 16 7"><rect x="0.5" y="0.5" width="13" height="6" fill="none" stroke="#111"/><rect x="2" y="2" width="10" height="3" fill="#111"/><rect x="14" y="2" width="1.5" height="3" fill="#111"/></svg>
    </div>
    <header class="app-header">
      <svg class="app-header__icon app-header__icon--back" width="14" height="14" viewBox="0 0 14 14"><path d="M1 7 L7 1 M1 7 L7 13 M1 7 H13" stroke="#fff" stroke-width="2.5" fill="none"/></svg>
      <span class="app-header__name">Trovanta</span>
      <svg class="app-header__icon app-header__icon--settings" width="15" height="15" viewBox="0 0 16 16"><circle cx="8" cy="8" r="5" fill="none" stroke="#fff" stroke-width="3.5" stroke-dasharray="2.6 1.6"/><circle cx="8" cy="8" r="4" fill="#fff"/><circle cx="8" cy="8" r="1.8" fill="#241008"/></svg>
    </header>
    <nav class="tabs">
      <span class="tab tab--challenges">Challenges</span>
      <span class="tab tab--completed">Completed</span>
    </nav>
    <ul class="challenge-list">
      <li class="challenge"><p class="challenge__title">Shoe shine</p><p class="challenge__points">3 points</p><svg class="challenge__chevron" width="8" height="12" viewBox="0 0 8 12"><path d="M1 1 L6 6 L1 11" stroke="#4db21f" stroke-width="2.5" fill="none"/></svg></li>
      <li class="challenge"><p class="challenge__title">Unicorn of the sea</p><p class="challenge__points">2 points</p><svg class="challenge__chevron" width="8" height="12" viewBox="0 0 8 12"><path d="M1 1 L6 6 L1 11" stroke="#4db21f" stroke-width="2.5" fill="none"/></svg></li>
      <li class="challenge"><p class="challenge__title">Reindeer</p><p class="challenge__points">2 points</p><svg class="challenge__chevron" width="8" height="12" viewBox="0 0 8 12"><path d="M1 1 L6 6 L1 11" stroke="#4db21f" stroke-width="2.5" fill="none"/></svg></li>
    </ul>
    <dl class="stats">
      <dt class="stats__label">Your Score :</dt><dd class="stats__value">2 points</dd>
      <dt class="stats__label">Time left :</dt><dd class="stats__value">58 minutes</dd>
      <dt class="stats__label">Challenges :</dt><dd class="stats__value">1&nbsp; of 30</dd>
    </dl>
  </section>
</body>
</html>
```